Postcard / Online add graphic

I'm doing a campaign and need a single design that I can put into different formats. I can do that part, I just need the creative part done.

Title: Feed the Social Media Monster with Great Photography
Content: You can take the content from my website: http://www.brindlelenswork.com/business-branding-photography/

Sample Images: https://www.parcelvault.net/sh/k7m2qx9wbtrflzc/QRT3H8k2pwmXcDdLbvHUen_5r?dl=0

Here is a Monster image I licensed for use for this project: https://www.parcelvault.net/s/4hw7ncr2lpzqvkd/stockorbit_xxl_technologymosters.jpg?dl=0

Logo is attached

I want it to be fun, colorful, graphical, and attention getting. Cartoonish is ok.

Target Market(s)

Business owners, social media managers

Industry/Entity Type

Campaign

Font styles to use
Sans Serif

Requirements
Must have
• Title and design on front
• Sales copy on back (whatever fits)
• Contact Information: Wade Pellinger, Photographer, (555) 314-7720, www.brindlelenswork.com

```html
<!DOCTYPE html>
<html lang="en">
<head>
<meta charset="utf-8">
<title>Feed the Social Media Monster – Postcard</title>
<link rel="stylesheet" href="https://fonts.googleapis.com/css2?family=Caveat:wght@400;500&family=Dancing+Script:wght@700&family=Montserrat:wght@400;500&display=swap">
<style>
  :root {
    --page: #eceff0;
    --card-dark: #0c0d0c;
    --card-deep: #141814;
    --white: #ffffff;
    --copy: #dcdcdc;
    --lime: #9fdc3c;
    --badge: #d6f21a;
    --gold-light: #f4e3a1;
    --gold: #c9a64a;
    --gold-dark: #8a6a22;
    --blue: #1f3fc4;
    --blue-light: #3a6df0;
  }
  * { box-sizing: border-box; margin: 0; padding: 0; }
  html, body { width: 848px; height: 1200px; overflow: hidden; background: var(--page); }
  body { position: relative; font-family: "Montserrat", sans-serif; }

  .card {
    position: absolute; left: 26px; width: 790px; height: 512px;
    background: radial-gradient(ellipse at 30% 40%, var(--card-deep), var(--card-dark) 70%);
    overflow: hidden;
  }
  .card--front { top: 26px; }
  .card--back { top: 614px; }
  .card__art { position: absolute; inset: 0; width: 790px; height: 512px; }

  /* Front */
  .frame { position: absolute; left: 20px; top: 20px; width: 370px; height: 200px; }
  .front__kicker {
    position: absolute; left: 42px; top: 46px; white-space: nowrap;
    font-family: "Caveat", cursive; font-size: 33px; color: var(--white); letter-spacing: 0.5px;
  }
  .front__title {
    position: absolute; font-family: "Dancing Script", cursive; font-weight: 700; line-height: 1; white-space: nowrap;
    background: linear-gradient(180deg, var(--gold-light) 0%, var(--gold) 55%, var(--gold-dark) 100%);
    -webkit-background-clip: text; background-clip: text; color: transparent;
  }
  .front__title--great { left: 38px; top: 96px; font-size: 68px; }
  .front__title--photo { left: 88px; top: 154px; font-size: 70px; }

  .brand {
    position: absolute; display: flex; align-items: center; gap: 10px; white-space: nowrap;
    color: var(--white); font-family: "Montserrat", sans-serif; font-weight: 400;
    letter-spacing: 3px; text-transform: uppercase; font-size: 15px;
  }
  .brand__dot { width: 12px; height: 12px; border-radius: 50%; background: var(--white); }
  .brand--front { left: 30px; top: 470px; }
  .brand--back { left: 20px; top: 456px; font-size: 14px; }

  /* Back */
  .back__heading {
    position: absolute; font-family: "Caveat", cursive; font-weight: 400;
    font-size: 33px; line-height: 1; color: var(--white); white-space: nowrap;
  }
  .back__heading--accent { color: var(--lime); }
  .back__copy {
    position: absolute; left: 393px; top: 110px; width: 374px;
    font-size: 12.4px; line-height: 1.24; color: var(--copy); text-align: justify; letter-spacing: 0.2px;
  }
  .benefits { position: absolute; left: 387px; top: 320px; width: 385px; list-style: none; }
  .benefits li {
    position: relative; padding-left: 22px; margin-bottom: 8px;
    font-size: 12.4px; line-height: 1.25; color: var(--copy); letter-spacing: 0.2px;
  }
  .benefits svg { position: absolute; left: 0; top: 2px; width: 13px; height: 11px; }

  .divider { position: absolute; top: 446px; width: 1px; height: 46px; background: #8a8a8a; }
  .contact-name { position: absolute; left: 277px; top: 442px; font-family: "Caveat", cursive; font-size: 32px; color: var(--white); white-space: nowrap; }
  .contact-role { position: absolute; left: 378px; top: 480px; font-family: "Caveat", cursive; font-size: 13px; color: var(--lime); white-space: nowrap; }
  .contact-line {
    position: absolute; left: 462px; display: flex; align-items: center; gap: 10px; white-space: nowrap;
    font-family: "Caveat", cursive; font-size: 23px; color: var(--white); letter-spacing: 0.5px;
  }
  .contact-line svg { width: 15px; height: 15px; }
  .contact-line--phone { top: 442px; }
  .contact-line--web { top: 470px; }
  .partner-badge { position: absolute; left: 710px; top: 430px; width: 66px; height: 66px; background: var(--badge); }
</style>
</head>
<body>

<section class="card card--front">
  <svg class="card__art" viewBox="0 0 790 512" xmlns="http://www.w3.org/2000/svg">
    <defs>
      <linearGradient id="g-store" x1="0" y1="0" x2="1" y2="1">
        <stop offset="0" stop-color="#c9d1d8"/><stop offset="0.5" stop-color="#6f8f5a"/><stop offset="1" stop-color="#b9c8d8"/>
      </linearGradient>
      <linearGradient id="g-jewel" x1="0" y1="0" x2="1" y2="1">
        <stop offset="0" stop-color="#d9b2ae"/><stop offset="0.6" stop-color="#7a6462"/><stop offset="1" stop-color="#2a2424"/>
      </linearGradient>
      <linearGradient id="g-food" x1="0" y1="0" x2="1" y2="0">
        <stop offset="0" stop-color="#e9dca8"/><stop offset="1" stop-color="#a8323a"/>
      </linearGradient>
      <linearGradient id="g-blue" x1="0" y1="0" x2="1" y2="1">
        <stop offset="0" stop-color="var(--blue-light)"/><stop offset="1" stop-color="var(--blue)"/>
      </linearGradient>
    </defs>
    <g role="img" aria-label="Photo: smiling dry-cleaning shop worker in a green polo among bagged garments">
      <path d="M100 385 C210 295 330 258 450 262 C560 268 610 335 700 420 L790 470 L790 512 L340 512 C260 450 180 405 100 385 Z" fill="url(#g-store)"/>
    </g>
    <path d="M370 256 C460 186 600 152 790 146 L790 166 C610 172 480 206 390 262 Z" fill="#050505"/>
    <g role="img" aria-label="Photo: smiling jewelry shop owner with glasses and an amber necklace">
      <path d="M390 262 C480 206 610 172 790 166 L790 462 C700 436 650 380 610 330 C560 280 480 256 390 262 Z" fill="url(#g-jewel)"/>
    </g>
    <path d="M585 150 C640 90 710 55 790 38 L790 58 C715 75 650 108 600 158 Z" fill="#050505"/>
    <g role="img" aria-label="Photo: plate of eggs benedict held by a server">
      <path d="M598 146 C650 92 715 58 790 40 L790 0 L700 0 C690 40 640 100 598 146 Z" fill="url(#g-food)"/>
    </g>
    <path d="M0 365 C130 348 260 400 340 512 L0 512 Z" fill="#050505"/>
    <path d="M0 378 C120 362 245 410 318 512 L0 512 Z" fill="url(#g-blue)"/>
    <path d="M0 400 C110 392 215 430 280 512 L250 512 C195 442 105 412 0 418 Z" fill="#4f86ff" opacity="0.35"/>
  </svg>

  <svg class="frame" viewBox="0 0 370 200" fill="none" stroke="#9a9a9a" stroke-width="1.2" aria-hidden="true">
    <path d="M1 14 V1 H24"/><path d="M346 1 H369 V14"/>
    <path d="M1 186 V199 H24"/><path d="M346 199 H369 V186"/>
    <circle cx="233" cy="120" r="10"/>
  </svg>

  <p class="front__kicker">Feed the Social Media Monster with</p>
  <h1 class="front__title front__title--great">Great</h1>
  <h1 class="front__title front__title--photo">Photography</h1>

  <div class="brand brand--front"><span class="brand__dot"></span>Brindle Lenswork</div>
</section>

<section class="card card--back">
  <svg class="card__art" viewBox="0 0 790 512" xmlns="http://www.w3.org/2000/svg">
    <defs>
      <linearGradient id="g-baker" x1="0" y1="0" x2="1" y2="1">
        <stop offset="0" stop-color="#b8a27a"/><stop offset="0.5" stop-color="#e6d5c6"/><stop offset="1" stop-color="#f2f0ee"/>
      </linearGradient>
      <linearGradient id="g-owner" x1="0" y1="0" x2="1" y2="0">
        <stop offset="0" stop-color="#2a5fb0"/><stop offset="0.6" stop-color="#8c6e5c"/><stop offset="1" stop-color="#c2402e"/>
      </linearGradient>
    </defs>
    <g role="img" aria-label="Photo: smiling bakery owner in an apron holding a strawberry cream pie">
      <path d="M0 0 H320 C300 90 330 190 345 245 C240 216 110 204 0 190 Z" fill="url(#g-baker)"/>
    </g>
    <g role="img" aria-label="Photo: smiling business owner in a blue polo in front of his shop">
      <path d="M0 214 C110 228 235 246 325 262 C300 330 250 380 200 410 H0 Z" fill="url(#g-owner)"/>
    </g>
  </svg>

  <h2 class="back__heading" style="left:395px;top:28px;">If you Market at all,</h2>
  <h2 class="back__heading back__heading--accent" style="left:475px;top:64px;">you need Great Images</h2>

  <p class="back__copy">Business Branding Photography sets you apart from your competitors by telling your story in a highly visual, engaging way. Whether its your website, social media sites, or your next postcard or print campaign, great photographs will visually show who you are and how you are different. That’s where we come in.</p>

  <h2 class="back__heading" style="left:392px;top:234px;">What can Business Branding</h2>
  <h2 class="back__heading back__heading--accent" style="left:505px;top:270px;">Photography do for you?</h2>

  <ul class="benefits">
    <li><svg viewBox="0 0 13 11" fill="none" stroke="var(--lime)" stroke-width="1.2"><rect x="0.6" y="2.4" width="11.8" height="8" rx="1"/><path d="M4 2.4 L5 0.8 H8 L9 2.4"/><circle cx="6.5" cy="6.4" r="2.2"/></svg>It tells your unique story in a fun, highly visual way</li>
    <li><svg viewBox="0 0 13 11" fill="none" stroke="var(--lime)" stroke-width="1.2"><rect x="0.6" y="2.4" width="11.8" height="8" rx="1"/><path d="M4 2.4 L5 0.8 H8 L9 2.4"/><circle cx="6.5" cy="6.4" r="2.2"/></svg>Helps you engage with your customers on web, social media and print</li>
    <li><svg viewBox="0 0 13 11" fill="none" stroke="var(--lime)" stroke-width="1.2"><rect x="0.6" y="2.4" width="11.8" height="8" rx="1"/><path d="M4 2.4 L5 0.8 H8 L9 2.4"/><circle cx="6.5" cy="6.4" r="2.2"/></svg>Sells more of your Products or Services</li>
  </ul>

  <div class="brand brand--back"><span class="brand__dot"></span>Brindle Lenswork</div>
  <span class="divider" style="left:260px;"></span>
  <p class="contact-name">Wade Pellinger</p>
  <p class="contact-role">Photographer</p>
  <span class="divider" style="left:450px;"></span>

  <p class="contact-line contact-line--phone">
    <svg viewBox="0 0 16 16" fill="none" stroke="var(--lime)" stroke-width="1.3"><path d="M3 1.5 L6 1.5 L7 5 L5.2 6.3 C6 8.3 7.7 10 9.7 10.8 L11 9 L14.5 10 L14.5 13 C14.5 14 13.6 14.6 12.6 14.5 C6.8 13.9 2.1 9.2 1.5 3.4 C1.4 2.4 2 1.5 3 1.5 Z"/></svg>
    (555) 314-7720
  </p>
  <p class="contact-line contact-line--web">
    <svg viewBox="0 0 16 16" fill="none" stroke="var(--lime)" stroke-width="1.2"><circle cx="8" cy="8" r="6.5"/><ellipse cx="8" cy="8" rx="3" ry="6.5"/><path d="M1.5 8 H14.5 M2.5 4.8 H13.5 M2.5 11.2 H13.5"/></svg>
    www.brindlelenswork.com
  </p>

  <div class="partner-badge" role="img" aria-label="Licensed monster artwork badge"></div>
</section>

</body>
</html>
```